Lift-Lantern needs a design for a new mobile app

A new app - lift-lantern.example, requires a design for its new app.

The app lets users add, create and share gym sessions. Sessions can be created, sets added and exercises chosen.

The app is currently functional on Android only (ios later), all that is required is a design for the app.

Some design assets are available (logo, colours, font), so the app should tie into these.

The design needs to be clean, simple and obvious, and all design assets will be required as part of this project.

One of the pages has % complete on the set - an icon to demonstrate this rather than a text based (eg 50%) would be great.

Screenshots will be available, along with the logos, colours and fonts.

Target Market(s)

Gym goers, all ages, male & female, fitness enthusiasts
Users of phones and tablets

Industry/Entity Type

Gym

Requirements
Must have
• Designs examples for each of the screens in the app, and an obvious selection of reusable elements (such as drop downs, radio buttons, buttons, calendar selectors, check boxes etc)
• Colours, logos and branding to fit into what is already available on the website.
• Usability and consistency are vital. Buttons should be in the same place (where possible).
• Design should help the user to complete the journey, and not get in the way.
• It should be a pleasure to use the app.
• Happy to have white space where appropriate.
• We use native elements where available.
Should not have
• Design features that waste space

```html
<!DOCTYPE html>
<html lang="en">
<head>
<meta charset="utf-8">
<title>Lift-Lantern – Dumbbell Curl Sets</title>
<link rel="stylesheet" href="https://fonts.googleapis.com/css2?family=Montserrat:wght@400;500;600&display=swap">
<style>
  :root {
    --page-bg: #f1f3f5;
    --status-blue: #0a84c8;
    --bar-blue: #1e91cd;
    --accent-blue: #1a8fd0;
    --fab-blue: #0b8fdc;
    --tab-bg: #efefef;
    --tab-text: #8a8a8a;
    --row-text: #7a7a7a;
    --muted: #a9a9a9;
    --divider: #e4e4e4;
    --box-border: #cfcfcf;
    --bin: #8c8c8c;
    --white: #ffffff;
  }
  * { box-sizing: border-box; margin: 0; padding: 0; }
  html, body {
    width: 1059px; height: 1200px; overflow: hidden;
    background: var(--page-bg);
    font-family: "Montserrat", "Helvetica Neue", Arial, sans-serif;
  }
  .app-screen {
    position: absolute; left: 212px; top: 35px;
    width: 635px; height: 1130px;
    background: var(--white);
    overflow: hidden;
    box-shadow: 0 2px 14px rgba(0,0,0,0.08);
  }
  .status-bar {
    height: 42px; background: var(--status-blue);
    display: flex; align-items: center; justify-content: flex-end;
    gap: 8px; padding-right: 12px; color: var(--white);
  }
  .status-time { font-size: 24px; font-weight: 500; margin-left: 8px; letter-spacing: 0.5px; }
  .app-bar {
    height: 88px; background: var(--bar-blue);
    display: flex; align-items: center; position: relative;
    box-shadow: 0 2px 3px rgba(0,0,0,0.12);
  }
  .back-button { position: absolute; left: 14px; top: 29px; }
  .screen-title {
    position: absolute; left: 89px; top: 28px;
    color: var(--white); font-size: 22px; font-weight: 600; letter-spacing: 0.2px;
  }
  .info-button { position: absolute; left: 516px; top: 30px; }
  .calendar-button { position: absolute; left: 597px; top: 30px; }
  .tab-bar {
    height: 53px; background: var(--tab-bg);
    display: flex; border-bottom: 1px solid var(--divider);
  }
  .tab {
    flex: 1; display: flex; align-items: center; justify-content: center;
    font-size: 20px; font-weight: 500; color: var(--tab-text);
    position: relative;
  }
  .tab + .tab::before {
    content: ""; position: absolute; left: 0; top: 10px; bottom: 10px;
    width: 1px; background: #dadada;
  }
  .tab.is-active { color: var(--accent-blue); }
  .tab.is-active::after {
    content: ""; position: absolute; left: 0; right: 0; bottom: -1px;
    height: 3px; background: var(--accent-blue);
  }
  .set-list { list-style: none; }
  .set-row {
    height: 70px; border-bottom: 1px solid var(--divider);
    position: relative; display: flex; align-items: center;
  }
  .set-label { position: absolute; left: 12px; font-size: 19px; color: var(--row-text); }
  .set-index { font-weight: 600; }
  .record-icon { position: absolute; left: 424px; }
  .done-box {
    position: absolute; left: 481px; width: 28px; height: 28px;
    border: 2px solid var(--box-border); background: var(--white);
  }
  .done-label { position: absolute; left: 528px; font-size: 19px; font-weight: 500; color: var(--muted); }
  .delete-icon { position: absolute; left: 600px; }
  .add-set-button {
    position: absolute; left: 541px; top: 1033px;
    width: 72px; height: 72px; border-radius: 50%;
    background: var(--fab-blue);
    box-shadow: 0 3px 6px rgba(0,0,0,0.22);
    display: flex; align-items: center; justify-content: center;
  }
</style>
</head>
<body>
<main class="app-screen">
  <div class="status-bar">
    <svg width="32" height="24" viewBox="0 0 32 24"><path d="M16 23 L1 5 Q16 -5 31 5 Z" fill="#fff"/></svg>
    <svg width="24" height="24" viewBox="0 0 24 24"><path d="M24 0 V24 H0 Z" fill="#fff"/></svg>
    <svg width="16" height="26" viewBox="0 0 16 26"><rect x="4" y="0" width="8" height="3" fill="#fff"/><rect x="0" y="2" width="16" height="24" rx="1" fill="#fff"/></svg>
    <span class="status-time">12:30</span>
  </div>

  <header class="app-bar">
    <svg class="back-button" width="32" height="28" viewBox="0 0 32 28" aria-label="Back"><path d="M30 14 H3 M14 3 L3 14 L14 25" fill="none" stroke="#fff" stroke-width="2.6"/></svg>
    <h1 class="screen-title">Dumbbell Curl</h1>
    <svg class="info-button" width="28" height="28" viewBox="0 0 28 28" aria-label="Exercise info"><circle cx="14" cy="14" r="13" fill="#fff"/><circle cx="14" cy="8" r="2" fill="var(--bar-blue)"/><rect x="12" y="11.5" width="4" height="10" fill="var(--bar-blue)"/></svg>
    <svg class="calendar-button" width="26" height="28" viewBox="0 0 26 28" aria-label="Choose date">
      <rect x="1.5" y="4" width="23" height="22" fill="none" stroke="#fff" stroke-width="2"/>
      <rect x="1.5" y="4" width="23" height="5" fill="#fff"/>
      <rect x="6" y="1" width="2.5" height="6" fill="#fff"/><rect x="17.5" y="1" width="2.5" height="6" fill="#fff"/>
      <g fill="#fff"><rect x="5" y="12" width="3" height="3"/><rect x="9.5" y="12" width="3" height="3"/><rect x="14" y="12" width="3" height="3"/><rect x="18.5" y="12" width="3" height="3"/><rect x="5" y="17" width="3" height="3"/><rect x="9.5" y="17" width="3" height="3"/><rect x="14" y="17" width="3" height="3"/><rect x="18.5" y="17" width="3" height="3"/></g>
    </svg>
  </header>

  <nav class="tab-bar">
    <div class="tab is-active">Sets</div>
    <div class="tab">History</div>
    <div class="tab">Records</div>
  </nav>

  <ul class="set-list">
    <li class="set-row">
      <span class="set-label"><span class="set-index">1.</span> 43.00 kg x 3</span>
      <svg class="record-icon" width="34" height="30" viewBox="0 0 34 30" aria-label="Personal record"><path d="M8 1 H26 V10 Q26 18 17 19 Q8 18 8 10 Z" fill="var(--accent-blue)"/><path d="M8 4 H2 Q2 13 10 14 M26 4 H32 Q32 13 24 14" fill="none" stroke="var(--accent-blue)" stroke-width="2.5"/><rect x="15" y="18" width="4" height="5" fill="var(--accent-blue)"/><rect x="9" y="23" width="16" height="6" rx="1" fill="var(--accent-blue)"/></svg>
      <span class="done-box"></span>
      <span class="done-label">Done</span>
      <svg class="delete-icon" width="22" height="28" viewBox="0 0 22 28" aria-label="Delete set"><rect x="7" y="0" width="8" height="3" fill="var(--bin)"/><rect x="0" y="3" width="22" height="3" fill="var(--bin)"/><path d="M2 8 H20 L19 28 H3 Z" fill="var(--bin)"/><g fill="#fff"><rect x="6" y="11" width="2" height="14"/><rect x="10" y="11" width="2" height="14"/><rect x="14" y="11" width="2" height="14"/></g></svg>
    </li>
    <li class="set-row">
      <span class="set-label"><span class="set-index">2.</span> 43.00 kg x 3</span>
      <svg class="record-icon" width="34" height="30" viewBox="0 0 34 30" aria-label="Personal record"><path d="M8 1 H26 V10 Q26 18 17 19 Q8 18 8 10 Z" fill="var(--accent-blue)"/><path d="M8 4 H2 Q2 13 10 14 M26 4 H32 Q32 13 24 14" fill="none" stroke="var(--accent-blue)" stroke-width="2.5"/><rect x="15" y="18" width="4" height="5" fill="var(--accent-blue)"/><rect x="9" y="23" width="16" height="6" rx="1" fill="var(--accent-blue)"/></svg>
      <span class="done-box"></span>
      <span class="done-label">Done</span>
      <svg class="delete-icon" width="22" height="28" viewBox="0 0 22 28" aria-label="Delete set"><rect x="7" y="0" width="8" height="3" fill="var(--bin)"/><rect x="0" y="3" width="22" height="3" fill="var(--bin)"/><path d="M2 8 H20 L19 28 H3 Z" fill="var(--bin)"/><g fill="#fff"><rect x="6" y="11" width="2" height="14"/><rect x="10" y="11" width="2" height="14"/><rect x="14" y="11" width="2" height="14"/></g></svg>
    </li>
  </ul>

  <div class="add-set-button" aria-label="Add set">
    <svg width="30" height="30" viewBox="0 0 30 30"><path d="M15 1 V29 M1 15 H29" stroke="#fff" stroke-width="2.6"/></svg>
  </div>
</main>
</body>
</html>
```